real esate business card with company logo and name

we need a business card design for a real esate company

The company name is Walsh & Brody Pty Ltd, and we have our logo designed and will upload. We want classic or moden feel. Black or white background. looks more textured. Should include folowinginformations
Paul Walsh and Lucy Brody
Sales Agents & Onsite Manager
p: 07 5948 2063
F: 07 5948 2174
M:0461 857 239
3/42 Marlin Crescent, HARLOW PARK QLD 4190

We want this business card looks professonal. Thank you in advance.

Industry/Entity Type

Real Estate Agent

Contact Information for Business Card

Paul Walsh and Lucy Brody
Onsite Manager & Sales Agents
p: 07 5948 2063
M:0461 857 239

Font styles to use
Serif

Colors
000000
fbfbfb
333333
959595

Requirements
Must have
• company logo and name, black or white back ground

```html
<!DOCTYPE html>
<html lang="en">
<head>
<meta charset="utf-8">
<title>Walsh &amp; Brody Pty Ltd — Business Card</title>
<link href="https://fonts.googleapis.com/css2?family=Oswald:wght@500&family=Open+Sans:wght@400;700&display=swap" rel="stylesheet">
<style>
  :root {
    --ink: #000000;
    --card: #0d0d0d;
    --paper-light: #fbfbfb;
    --charcoal: #333333;
    --mid-grey: #959595;
    --stage: #e6e4e1;
  }
  * { box-sizing: border-box; margin: 0; padding: 0; }
  html, body { width: 1200px; height: 720px; overflow: hidden; }
  body {
    background: var(--stage);
    display: flex;
    align-items: center;
    justify-content: center;
    gap: 40px;
  }
  .card {
    position: relative;
    width: 540px;
    height: 310px;
    border-radius: 4px;
    background-color: var(--card);
    background-image:
      radial-gradient(rgba(255,255,255,0.035) 1px, transparent 1px),
      radial-gradient(rgba(255,255,255,0.025) 1px, transparent 1px);
    background-size: 3px 3px, 5px 5px;
    background-position: 0 0, 1px 2px;
    box-shadow: 0 10px 28px rgba(0,0,0,0.28);
    overflow: hidden;
  }
  .mark {
    display: flex;
    align-items: center;
    gap: 10px;
    font-family: "Oswald", sans-serif;
    font-weight: 500;
    color: var(--mid-grey);
    letter-spacing: 0.04em;
    font-size: 24px;
    line-height: 1;
    white-space: nowrap;
  }
  .mark-square {
    width: 28px;
    height: 28px;
    background: var(--mid-grey);
    flex: none;
  }
  .company-name {
    font-family: "Oswald", sans-serif;
    font-weight: 500;
    color: var(--mid-grey);
    font-size: 16px;
    letter-spacing: 0.03em;
    text-transform: uppercase;
    margin-top: 14px;
    white-space: nowrap;
  }

  /* Front */
  .card-front {
    display: flex;
    flex-direction: column;
    align-items: center;
    justify-content: center;
  }

  /* Back */
  .card-back .brand {
    position: absolute;
    left: 36px;
    top: 104px;
  }
  .contact {
    position: absolute;
    left: 292px;
    top: 84px;
    font-family: "Open Sans", sans-serif;
    color: var(--mid-grey);
    font-size: 12.5px;
    line-height: 1.5;
    white-space: nowrap;
  }
  .contact-names {
    font-weight: 700;
    color: var(--paper-light);
    font-size: 14px;
    letter-spacing: 0.04em;
    text-transform: uppercase;
  }
  .contact-role { margin-bottom: 10px; }
  .contact-address { margin-bottom: 10px; }
  .contact-line {
    display: flex;
    align-items: center;
    gap: 8px;
  }
  .contact-line svg {
    width: 12px;
    height: 12px;
    fill: var(--mid-grey);
    flex: none;
  }
</style>
</head>
<body>

  <section class="card card-front">
    <div class="mark"><span class="mark-square"></span>WALSH &amp; BRODY</div>
    <p class="company-name">Walsh &amp; Brody Pty Ltd.</p>
  </section>

  <section class="card card-back">
    <div class="brand">
      <div class="mark"><span class="mark-square"></span>WALSH &amp; BRODY</div>
      <p class="company-name">Walsh &amp; Brody Pty Ltd.</p>
    </div>

    <div class="contact">
      <p class="contact-names">Paul Walsh | Lucy Brody</p>
      <p class="contact-role">Onsite Manager &amp; Sales Agents</p>
      <p class="contact-address">3/42 Marlin Crescent,<br>HARLOW PARK QLD 4190</p>
      <p class="contact-line">
        <svg viewBox="0 0 12 12" aria-hidden="true"><path d="M3 0h6a1 1 0 0 1 1 1v10a1 1 0 0 1-1 1H3a1 1 0 0 1-1-1V1a1 1 0 0 1 1-1zm0 1.5v8h6v-8z"/></svg>
        0461 857 239
      </p>
      <p class="contact-line">
        <svg viewBox="0 0 12 12" aria-hidden="true"><path d="M1 4c0-2 2-3 5-3s5 1 5 3v1H8.5V3.8h-5V5H1zM3 6h6l2 4v1H1v-1z"/></svg>
        07 5948 2063
      </p>
      <p class="contact-line">
        <svg viewBox="0 0 12 12" aria-hidden="true"><path d="M3 0h6v3H3zM1 4h10v6H9v2H3v-2H1zm3 4v3h4V8z"/></svg>
        07 5948 2174
      </p>
    </div>
  </section>

</body>
</html>
```